Etiketten-Design für Fruchtsaft-Schorlen und Cider
Wir sind total happy mit dem, was wir bekommen haben. Insgesamt fünf Designs, die absolut top waren und super gepasst haben. Wir hatten das Luxusproblem uns für eines der fünf zu entscheiden. Weil die Qualität dermaßen gut war, haben wir uns entschieden nochmals den Betrag des Preisgelds in die Hand zu nehmen und auf Platz 2 bis 4 unseres internen Rankings zu verteilen. Nämlich die Hälfte auf Platz 2 und jeweils ein Viertel auf die beiden dritten Plätze.
Zielgruppe
Wir sind ein landwirtschaftlicher Betrieb mit Fokus auf den Hochstamm-Feldobstbau, landläufig Streuobst genannt. Wir sind in Tübingen gelegen, im Zentrum des Alblinger Baumwiesenreiches (1).
Unsere Obsternte verarbeiten wir zu Fruchtsaft-Schorlen und Cider. Unter den Getränkeherstellern sind wir ein mikrokleiner Zwerg. Allerdings wird die Qualität unserer Getränke überragend hoch gelobt. Dazu trägt in wesentlichem Maße die außerordentliche Fruchtgüte unserer oftmals mehr als hundert Jahre alten Apfel- und Birnbäume bei. Deren altbewährten Sorten haben sich seit Generationen als besonders geeignet für die Saft- und Obstwein-Produktion erwiesen. Auch bei den zahlreichen Neupflanzung setzen wir nur auf diese traditionellen Sorten.
Für unser neues Produkt 'Hainperle' benötigen wir Flaschenetiketten, ein Bauchetikett und ein Rückenetikett.
Most, zur Erklärung, ist die schwäbische Variante des Apfelweins. Weitere regionale Varianten: Hessen Ebbelwoi, Saarland Viez, Frankreich Cidre, Spanien Sidra und im angelsächsischen Sprachraum Cider. Im Gegensatz zu Apfelwein wird Schwäbischer Most nicht allein aus Äpfeln sondern aus einer Mischung von Äpfeln, Birnen und (manchmal) Quitten gemacht.
Most hat ein sehr schlechtes Image. Einstmals das Volksgetränk schlechthin, mittlerweile praktisch bedeutungslos. Dies nicht ganz unverschuldet, weil oft in sehr nachlässiger Art hergestellt. Unser Most ist tadellos gut und hat das Potential Freunde zurückzugewinnen oder neu zu gewinnen.
Unsere Zielgruppe sind alle, die ein leicht alkoholisches Getränk möchten; Beispiel Weinschorle. Der Vertrieb beschränkt sich auf unser lokales Einzugsgebiet, ergänzt durch ein wenig Internetvertrieb.
Um sich in's Produkt eingrooven zu können verschicken wir gerne eine Kostprobe - nachdem eine Etiketten-Arbeitsprobe vorliegt, die gefällt. :-)
Mehr Info:
(1) https://www.baumwiesenreich.de/
(2)https://www.k..
Aufgabenstellung
Die neuen Etiketten dürfen anders oder völlig anders aussehen als die Etiketten unserer bereits vorhandenen Produkte. Als Inspiration gerne Cider- und/oder Biermarken heranziehen. Firmenfarbe grün soll berücksichtigt werden. Firmenschrift Garamond weitgehend ebenso. Wenn runde oder ovale Gestaltung, dann auf einem rechteckigem Fond, weil wir nur rechteckige Etiketten verarbeitet werden können.
Bei der betreffenden Flasche handelt es sich um die weit verbreitete 0,33-Liter-Longneck-Flasche, Glasfarbe braun.
Flaschenverschluß durch Kronkorken. Es kann unter folgenden Kronkorken-Farben gewählt werden: silber, altgold, gelb, weiß, rot, orange, schwarz.
Grafikdateien sind beigefügt für: Firmenlogo, Unterstützer-Logos, Nährwerte-QR-Code, Mehrweg-Logo, Barcode
Texte und Inhalte für Rückenetikett siehe beigefügte Datei.
Zum Bauchetikett haben wir kein Briefing gemacht, um der Kreativität freien Lauf zu lassen.
Technische Angaben zu den Etiketten:
Abmessung Bauchetikett: 85mm hoch x 80 mm breit
Abmessung Rückenetikett: 70mm hoch x 60mm breit

```html
<!DOCTYPE html>
<html lang="de">
<head>
<meta charset="utf-8">
<title>Lindhofer Hainperle 0,33L – Bauchetikett</title>
<link rel="stylesheet" href="https://fonts.googleapis.com/css2?family=EB+Garamond:ital,wght@0,500;0,700;1,400&family=Open+Sans:ital,wght@0,400;1,400&display=swap">
<style>
  :root {
    --brand-green: #136b35;
    --leaf-green: #93c01f;
    --paper: #ffffff;
    --ink: #1d1d1b;
    --glass-light: #e8701f;
    --glass-mid: #b8421a;
    --glass-dark: #3a1a0e;
    --cap: #c9c9c9;
    --heart: #d0202e;
  }
  * { box-sizing: border-box; margin: 0; padding: 0; }
  html, body { width: 855px; height: 1200px; overflow: hidden; background: var(--paper); }
  .sheet { position: relative; width: 855px; height: 1200px; background: var(--paper); }

  .sheet-brand {
    position: absolute; left: 50px; top: 44px;
    font-family: "EB Garamond", serif; font-weight: 500;
    font-size: 58px; line-height: 1; color: var(--brand-green);
  }
  .sheet-intro {
    position: absolute; left: 57px; top: 143px;
    font-family: "Open Sans", sans-serif; font-size: 14px; line-height: 20px; color: var(--ink);
  }
  .fruit-row {
    position: absolute; left: 667px; top: 48px; width: 155px; height: 48px;
    background: linear-gradient(90deg, #efefef, #dcdcdc, #efefef); border-radius: 24px;
  }

  .bottle { position: absolute; left: 428px; top: 120px; width: 275px; height: 1040px; }

  .label {
    position: absolute; left: 408px; top: 648px; width: 322px; height: 340px;
    background: var(--brand-green); overflow: hidden;
  }
  .label-paper {
    position: absolute; left: 12px; top: 10px; right: 12px; bottom: 8px;
    background: var(--paper);
    border-radius: 3px 6px 2px 5px;
  }
  .label-stripe {
    position: absolute; left: 83px; top: 0; width: 165px; height: 340px;
    background: var(--leaf-green);
  }
  .label-brand {
    position: absolute; left: 83px; width: 165px; top: 20px; text-align: center;
    font-family: "EB Garamond", serif; font-weight: 500; font-size: 29px; line-height: 1;
    color: var(--brand-green);
  }
  .label-sub {
    position: absolute; left: 83px; width: 165px; top: 52px; text-align: center;
    font-family: "EB Garamond", serif; font-weight: 700; font-size: 10px; line-height: 12px;
    letter-spacing: 5px; color: var(--ink);
  }
  .product-name {
    position: absolute; text-align: center;
    font-family: "EB Garamond", serif; font-weight: 700; line-height: 1;
    white-space: nowrap;
  }
  .product-name--top {
    left: 83px; width: 165px; top: 98px; font-size: 40px; letter-spacing: 1px;
    color: var(--paper); text-shadow: 0 0 8px rgba(255,255,255,.6);
  }
  .product-name--bottom {
    left: 0; width: 322px; top: 136px; font-size: 46px; letter-spacing: -1px;
    color: var(--brand-green);
  }

  .fruit-band {
    position: absolute; left: 0; top: 186px; width: 322px; height: 84px;
    background: linear-gradient(90deg, rgba(240,240,240,.85), rgba(120,160,40,.45) 40%, rgba(120,160,40,.45) 60%, rgba(240,240,240,.85));
  }
  .tagline {
    position: absolute; left: 83px; width: 165px; top: 284px; text-align: center;
    font-family: "Open Sans", sans-serif; font-style: italic; font-size: 10.5px; line-height: 14px;
    color: var(--paper);
  }
  .tagline svg { vertical-align: -3px; }
  .volume {
    position: absolute; left: 258px; top: 302px;
    font-family: "EB Garamond", serif; font-weight: 700; font-size: 14px; line-height: 1;
    color: var(--brand-green);
  }
</style>
</head>
<body>
<main class="sheet">
  <div class="sheet-brand">Lindhofer</div>
  <p class="sheet-intro">Lindhofer Hainperle 0,33L<br>Aus dem Herzen<br>des Alblinger Baumwiesenreiches</p>
  <div class="fruit-row" role="img" aria-label="Zeichnung einer Reihe von Äpfeln und Birnen"></div>

  <svg class="bottle" viewBox="0 0 275 1022" preserveAspectRatio="none" role="img" aria-label="Braune 0,33-Liter-Longneck-Flasche mit Kronkorken">
    <defs>
      <linearGradient id="glass" x1="0" x2="1">
        <stop offset="0" stop-color="var(--glass-dark)"/>
        <stop offset=".12" stop-color="var(--glass-mid)"/>
        <stop offset=".45" stop-color="var(--glass-light)"/>
        <stop offset=".85" stop-color="var(--glass-mid)"/>
        <stop offset="1" stop-color="var(--glass-dark)"/>
      </linearGradient>
    </defs>
    <path fill="url(#glass)" d="M76 28 H196 V70 Q198 80 194 90 L200 300 Q204 370 240 420 Q264 450 264 510 V1000 Q264 1017 240 1017 H34 Q10 1017 10 1000 V510 Q10 450 34 420 Q70 370 74 300 L80 90 Q76 80 78 70 Z"/>
    <rect x="72" y="4" width="128" height="30" rx="6" fill="var(--cap)"/>
  </svg>

  <section class="label">
    <div class="label-paper"></div>
    <div class="label-stripe"></div>
    <div class="label-brand">Lindhofer</div>
    <div class="label-sub">Streuobst</div>
    <div class="product-name product-name--top">HAIN</div>
    <div class="product-name product-name--bottom">PERLE</div>
    <div class="fruit-band" role="img" aria-label="Zeichnung von Äpfeln und Birnen mit Blättern"></div>
    <p class="tagline">Aus dem <svg width="16" height="14" viewBox="0 0 16 14"><path d="M8 13 C3 9 1 7 1 4.5 A3.3 3.3 0 0 1 8 3 A3.3 3.3 0 0 1 15 4.5 C15 7 13 9 8 13Z" fill="none" stroke="var(--heart)" stroke-width="1.3"/></svg> des Alblinger<br>Baumwiesenreiches</p>
    <div class="volume">0,33L</div>
  </section>
</main>
</body>
</html>
```